Create a flyer that will catch your eye and make you want to call us for KELVOTH seamless Gutters

We are looking for a logo to help us with sales of our seamless gutter business, we are looking to expand, add loyal customers and increase our referral business.
We provide a turn key process from sales to install. we show up with our rolling factory, our truck spits out what seems to be an endless supply of gutter!
Each job is fabricated and installed to meet your homes design.

Target Market(s)

Treasure Coast of Florida, single story Homes

Font styles to use
Serif

Requirements
Must have
• Our Logo and Name on the flyer
Clean design with a clear message
call to action

```html
<!DOCTYPE html>
<html lang="en">
<head>
<meta charset="utf-8">
<title>Kelvoth Gutters Flyer</title>
<link rel="stylesheet" href="https://fonts.googleapis.com/css2?family=Bebas+Neue&family=Raleway:wght@400;500&display=swap">
<style>
  :root {
    --backdrop: #d6d6d6;
    --paper: #f8f8f8;
    --brand-green: #2fa84f;
    --badge-green: #4cc47f;
    --ink-grey: #6a6a6a;
    --body-grey: #5a5a5a;
    --frame-grey: #8c8c8c;
    --white: #ffffff;
  }
  * { margin: 0; padding: 0; box-sizing: border-box; }
  html, body { width: 1200px; height: 900px; overflow: hidden; }
  body { background: var(--backdrop); position: relative; font-family: "Raleway", sans-serif; }

  .flyer {
    position: absolute; left: 319px; top: 20px;
    width: 562px; height: 860px;
    background: var(--paper);
    overflow: hidden;
    box-shadow: 0 4px 18px rgba(0,0,0,0.18);
  }
  .gear-art { position: absolute; left: 0; top: 0; width: 562px; height: 860px; }

  .brand {
    position: absolute; left: 34px; top: 66px;
    display: flex; align-items: center; gap: 8px;
    white-space: nowrap;
  }
  .brand-dot { width: 26px; height: 26px; border-radius: 50%; background: var(--frame-grey); flex: none; }
  .brand-name {
    font-family: "Bebas Neue", sans-serif; font-size: 34px; line-height: 1;
    color: var(--brand-green);
  }

  .warranty {
    position: absolute; left: 31px; top: 162px; width: 240px;
    text-align: center; font-family: "Bebas Neue", sans-serif; color: var(--ink-grey);
    white-space: nowrap;
  }
  .warranty-lead, .warranty-tail { font-size: 24px; line-height: 32px; }
  .warranty-word { font-size: 64px; line-height: 58px; color: var(--brand-green); margin: 2px 0 2px; }

  .estimate {
    position: absolute; left: 333px; top: 36px; width: 204px;
    text-align: center; color: var(--white);
  }
  .estimate-lead { font-family: "Bebas Neue", sans-serif; font-size: 30px; line-height: 32px; white-space: nowrap; }
  .estimate-lead strong { font-weight: 400; }
  .estimate-rule { width: 54px; height: 1px; background: var(--white); margin: 6px auto 4px; }
  .estimate-sub { font-size: 9.5px; letter-spacing: 0.2px; white-space: nowrap; }
  .estimate-protocol { font-family: "Bebas Neue", sans-serif; font-size: 31px; line-height: 31px; margin-top: 2px; white-space: nowrap; }
  .estimate-note { width: 172px; margin: 4px auto 0; font-size: 8.8px; line-height: 13px; }

  .about {
    position: absolute; left: 365px; top: 346px; width: 172px;
    font-size: 10.4px; line-height: 14.7px; color: var(--body-grey); text-align: justify;
  }

  .contact { position: absolute; left: 27px; top: 722px; width: 150px; color: var(--body-grey); }
  .contact-title { font-family: "Bebas Neue", sans-serif; font-size: 34px; line-height: 34px; color: var(--brand-green); }
  .contact-rule { width: 62px; height: 1.5px; background: var(--brand-green); margin: 2px 0 6px; }
  .contact-list { list-style: none; font-size: 9.6px; line-height: 11.6px; white-space: nowrap; }
  .contact-list li { display: flex; align-items: center; gap: 4px; }
  .contact-icon { width: 9px; height: 9px; flex: none; }
  .contact-divider { width: 40px; height: 1px; background: var(--body-grey); margin: 4px 0 5px; }
  .contact-address { font-size: 9.6px; line-height: 11.8px; white-space: nowrap; }
</style>
</head>
<body>
<main class="flyer">
  <svg class="gear-art" viewBox="0 0 562 860">
    <defs>
      <polygon id="gear-tooth" points="-15.5,-78 -4,-100 4,-100 15.5,-78"/>
      <g id="gear">
        <circle r="80"/>
        <use href="#gear-tooth"/>
        <use href="#gear-tooth" transform="rotate(22.5)"/>
        <use href="#gear-tooth" transform="rotate(45)"/>
        <use href="#gear-tooth" transform="rotate(67.5)"/>
        <use href="#gear-tooth" transform="rotate(90)"/>
        <use href="#gear-tooth" transform="rotate(112.5)"/>
        <use href="#gear-tooth" transform="rotate(135)"/>
        <use href="#gear-tooth" transform="rotate(157.5)"/>
        <use href="#gear-tooth" transform="rotate(180)"/>
        <use href="#gear-tooth" transform="rotate(202.5)"/>
        <use href="#gear-tooth" transform="rotate(225)"/>
        <use href="#gear-tooth" transform="rotate(247.5)"/>
        <use href="#gear-tooth" transform="rotate(270)"/>
        <use href="#gear-tooth" transform="rotate(292.5)"/>
        <use href="#gear-tooth" transform="rotate(315)"/>
        <use href="#gear-tooth" transform="rotate(337.5)"/>
      </g>
      <linearGradient id="leaf-gutter-tone" x1="0" y1="0" x2="1" y2="1">
        <stop offset="0" stop-color="#85857f"/>
        <stop offset="0.5" stop-color="#9c8d76"/>
        <stop offset="1" stop-color="#6f706b"/>
      </linearGradient>
      <linearGradient id="roof-tone" x1="0" y1="0" x2="0" y2="1">
        <stop offset="0" stop-color="#9ab0a8"/>
        <stop offset="0.3" stop-color="#cf6a4f"/>
        <stop offset="0.6" stop-color="#b77a55"/>
        <stop offset="1" stop-color="#dccbb2"/>
      </linearGradient>
      <linearGradient id="guard-tone" x1="0" y1="0" x2="1" y2="1">
        <stop offset="0" stop-color="#a4a894"/>
        <stop offset="1" stop-color="#e2e2de"/>
      </linearGradient>
    </defs>

    <use class="badge-gear" href="#gear" fill="var(--badge-green)" transform="translate(440 125) scale(1.9) rotate(6)"/>

    <g class="photo-gear" role="img" aria-label="Photo of a white gutter clogged with dry leaves beside slate roof tiles">
      <use href="#gear" fill="var(--frame-grey)" transform="translate(180 528) scale(1.9)"/>
      <use href="#gear" fill="url(#leaf-gutter-tone)" transform="translate(180 528) scale(1.82)"/>
    </g>

    <g class="photo-gear" role="img" aria-label="Photo of a red tiled roof edge with a copper gutter and downspout">
      <use href="#gear" fill="var(--frame-grey)" transform="translate(437 672) scale(1.33) rotate(8)"/>
      <use href="#gear" fill="url(#roof-tone)" transform="translate(437 672) scale(1.26) rotate(8)"/>
    </g>

    <g class="photo-gear" role="img" aria-label="Photo of a perforated gutter guard along a mossy roof">
      <use href="#gear" fill="var(--brand-green)" transform="translate(267 788) scale(0.8) rotate(4)"/>
      <use href="#gear" fill="url(#guard-tone)" transform="translate(267 788) scale(0.73) rotate(4)"/>
    </g>
  </svg>

  <div class="brand">
    <span class="brand-dot"></span>
    <span class="brand-name">Kelvoth Gutters</span>
  </div>

  <section class="warranty">
    <p class="warranty-lead">We provide the very best</p>
    <p class="warranty-word">Warranty</p>
    <p class="warranty-tail">In the business and use the<br>best materials available.</p>
  </section>

  <section class="estimate">
    <p class="estimate-lead">We provide <strong>free</strong> in<br>home estimates</p>
    <div class="estimate-rule"></div>
    <p class="estimate-sub">AND ARE ADHERING TO</p>
    <p class="estimate-protocol">Stringent COVID-19<br>protocals</p>
    <p class="estimate-note">Someone is always available to answer your calls, provide answers to your questions and update you on the progress of your job</p>
  </section>

  <p class="about">Kelvoth Gutters provides top quality seamless gutter system that will protect your home for many years. Our traveling gutter factory on wheels allows us to custom fit gutters to your homes specific needs at a competitive price. We take pride in our excellent customer service, professional installs and quality products.</p>

  <section class="contact">
    <h2 class="contact-title">Contact us</h2>
    <div class="contact-rule"></div>
    <ul class="contact-list">
      <li>
        <svg class="contact-icon" viewBox="0 0 10 10"><circle cx="5" cy="5" r="5" fill="var(--brand-green)"/><path d="M3.2 2.6 L4.2 3.8 L3.7 4.4 Q4.6 5.8 5.6 6.3 L6.2 5.8 L7.4 6.8 L6.7 7.6 Q4 7 2.5 3.4 Z" fill="var(--white)"/></svg>
        +0123 456 789
      </li>
      <li>
        <svg class="contact-icon" viewBox="0 0 10 10"><circle cx="5" cy="5" r="5" fill="var(--brand-green)"/><rect x="2.4" y="3.2" width="5.2" height="3.6" fill="none" stroke="var(--white)" stroke-width="0.8"/><path d="M2.4 3.2 L5 5.2 L7.6 3.2" fill="none" stroke="var(--white)" stroke-width="0.8"/></svg>
        info@kelvothgutters.com
      </li>
      <li>
        <svg class="contact-icon" viewBox="0 0 10 10"><circle cx="5" cy="5" r="5" fill="var(--brand-green)"/><circle cx="5" cy="5" r="2.6" fill="none" stroke="var(--white)" stroke-width="0.7"/><path d="M2.4 5 H7.6 M5 2.4 V7.6" stroke="var(--white)" stroke-width="0.7"/></svg>
        www.kelvothgutters.com
      </li>
    </ul>
    <div class="contact-divider"></div>
    <p class="contact-address">Your address, Suit # 000,<br>Dummy Street, City, State,</p>
  </section>
</main>
</body>
</html>
```